New Business Cards for MB&LR

We need updated business cards for a staff of 15 engineers, estimators, project managers, and sales people. We have recently begun changes to our website and marketing material to improve our look and branding. We are an established fabricator specializing in pressure vessels, tanks, and structural steel. The owners require us to use the existing logo and old english text design. Also, we prefer dark grey or mostly black cards.
Target Market(s)
Engineers, purchasing agents, estimators, and project managers of; mining companies, refineries, industrial construction professionals
Industry/Entity Type
Business
Contact Information for Business Card
Logo, phone, website, email, etc.
Look and feel

```html
<!DOCTYPE html>
<html lang="en">
<head>
<meta charset="utf-8">
<title>MB&amp;LR Business Card</title>
<link rel="stylesheet" href="https://fonts.googleapis.com/css2?family=Oswald:wght@600&family=Work+Sans:wght@400;500&display=swap">
<style>
  :root {
    --backdrop: #3a302a;
    --card: #0e0e0e;
    --ink: #f4f4f4;
    --ink-soft: #cfcfcf;
    --silver: #c9c9c9;
    --rule: #e6e6e6;
  }
  * { margin: 0; padding: 0; box-sizing: border-box; }
  html, body {
    width: 1200px; height: 715px; overflow: hidden;
    background: var(--backdrop);
    font-family: "Work Sans", sans-serif;
  }
  .sheet {
    width: 1200px; height: 715px;
    display: flex; align-items: center; justify-content: center; gap: 48px;
  }
  .card {
    width: 525px; height: 300px;
    background: var(--card);
    border-radius: 6px;
    position: relative;
    box-shadow: 0 10px 30px rgba(0,0,0,.45);
  }
  .card-front { display: flex; align-items: center; justify-content: center; }
  .brand-mark {
    font-family: "Work Sans", sans-serif;
    font-weight: 500; font-size: 34px; letter-spacing: 3px;
    color: var(--silver);
  }
  .identity {
    position: absolute; left: 70px; top: 92px;
    text-align: right; width: 190px;
  }
  .identity-name {
    font-family: "Oswald", sans-serif; font-weight: 600;
    font-size: 34px; line-height: 1; letter-spacing: .5px;
    color: var(--ink); text-transform: uppercase; white-space: nowrap;
  }
  .identity-role {
    font-size: 12px; letter-spacing: 1.5px; color: var(--ink-soft);
    text-transform: uppercase; margin-top: 6px; padding-right: 22px;
  }
  .divider {
    position: absolute; left: 285px; top: 92px;
    width: 1px; height: 56px; background: var(--rule);
  }
  .contact-list {
    position: absolute; left: 305px; top: 108px;
    list-style: none; color: var(--ink);
    font-size: 15px; line-height: 20px; letter-spacing: .3px;
  }
  .contact-list li { display: flex; align-items: center; gap: 8px; }
  .contact-list svg { width: 10px; height: 10px; fill: var(--ink); flex: none; }
  .seal {
    position: absolute; left: 28px; bottom: 56px;
    display: flex; align-items: center; gap: 6px;
    font-size: 10px; font-weight: 500; color: var(--silver); letter-spacing: 1px;
  }
  .seal-dot { width: 22px; height: 22px; border-radius: 50%; background: var(--silver); }
  .address {
    position: absolute; left: 78px; bottom: 40px;
    font-size: 14px; color: var(--ink); letter-spacing: .3px;
  }
</style>
</head>
<body>
  <main class="sheet">
    <section class="card card-front">
      <span class="brand-mark">MB&amp;LR</span>
    </section>

    <section class="card card-back">
      <div class="identity">
        <div class="identity-name">Owen Hale</div>
        <div class="identity-role">Director</div>
      </div>
      <div class="divider"></div>
      <ul class="contact-list">
        <li>
          <svg viewBox="0 0 10 10" aria-hidden="true"><path d="M2 0.5h2l.6 2.2-1.2.8a5 5 0 0 0 3 3l.8-1.2 2.2.6v2c0 .6-.5 1.1-1.1 1.1A8 8 0 0 1 .9 1.6C.9 1 1.4.5 2 .5z"/></svg>
          555.214.7730
        </li>
        <li>
          <svg viewBox="0 0 10 10" aria-hidden="true"><rect x="2.5" y="0" width="5" height="10" rx="1"/></svg>
          555.218.4406
        </li>
        <li>
          <svg viewBox="0 0 10 10" aria-hidden="true"><path d="M0 2h10v6H0z M1 3v.3l4 2.5 4-2.5V3l-4 2.4z" fill-rule="evenodd"/></svg>
          owen@mbandlr.com
        </li>
      </ul>
      <div class="seal"><span class="seal-dot"></span>MB&amp;LR</div>
      <p class="address">48 Foundry Road North Ridge Valley, UT 84000</p>
    </section>
  </main>
</body>
</html>
```